Double-Sided Table Top Flyer to Match Attached Marketing Materials

Please read this carefully. Must follow instructions. Do not submit multiple designs that look similar. Submit the front and back together as one submission. Do not submit the front and back separately. I have attached my new rack card design, business card design and gift card design. Colors, shapes and style match. I want a table top flyer to match them using same colors, shapes and style. The flyer will be 282.4 mm tall by 218.9 mm wide. See attached FLYER SPECs which shows full bleed, trim and safety area dimensions. THE FRONT: The main focus of the front is an "Lagoon Voyage Drawing". This should be the main focus / font centered on the front. Under this there should be the attached paragraph. The front will also use the attached "PROFILE PIRATE" picture. The front will also incorporate my primary logo for "Harbor Finch Sailing School & Cruises, LLC" as well as the badges of "Licensed Captain", "Instructor" and "Licensed Captain". Please incorporate the attached family beach day photo somehow. It may be set in the background as transparent. Designer's choice of how to incorporate. FOR THE BACK: Take most of the content from the front of the attached rack card. If additional content is required for the back please include as much as you can from the back of the attached rack card. The front has the three small pictures. The back has the one picture of me and the three logos towards the bottom. The content on the front of rack card takes priority over the content on back.

Target Market(s)

see attachments.

Industry/Entity Type

see attachments.

Font styles to use
Other font styles liked:
• The font type I use most is Good Timing RG from typecrate-sample.com

Requirements
Must have
• see attachments.
Nice to have
• see attachments.
Should not have
• see attachments.

```html
<!DOCTYPE html>
<html lang="en">
<head>
<meta charset="utf-8">
<title>Lagoon Voyage Drawing – Table Top Flyer</title>
<link href="https://fonts.googleapis.com/css2?family=Krona+One&family=Poppins:ital,wght@0,400;0,500;0,600;0,700;1,700&display=swap" rel="stylesheet">
<style>
  :root {
    --stage: #858585;
    --paper: #ffffff;
    --red: #e0193f;
    --navy: #1b1f3d;
    --gold: #e3b82a;
    --charcoal: #2b2b2d;
    --slate: #3b3b3e;
    --ink: #1e1e22;
    --mist: #eeeeef;
  }
  * { box-sizing: border-box; margin: 0; padding: 0; }
  html, body { width: 1200px; height: 762px; overflow: hidden; background: var(--stage); }
  body { position: relative; font-family: "Poppins", sans-serif; color: var(--ink); }

  .page { position: absolute; background: var(--paper); overflow: hidden; }
  .page--front { left: 69px; top: 49px; width: 508px; height: 655px; }
  .page--back  { left: 629px; top: 48px; width: 510px; height: 658px; }
  .page__shapes { position: absolute; inset: 0; width: 100%; height: 100%; }

  .display { font-family: "Krona One", sans-serif; text-transform: uppercase; line-height: 1; }

  /* Front */
  .title { position: absolute; left: 33px; top: 44px; }
  .title__line { display: block; color: var(--paper); }
  .title__line--lead { color: var(--gold); font-size: 43px; }
  .title__line--mid { font-size: 39px; margin-top: 6px; }
  .title__line--last { font-size: 35px; margin-top: 7px; }

  .intro { position: absolute; left: 34px; top: 182px; font-size: 9.4px; line-height: 11.8px; color: var(--ink); }
  .intro span { display: block; white-space: nowrap; }

  .brand-seal { position: absolute; left: 400px; top: 23px; width: 94px; height: 94px; border-radius: 50%;
    background: var(--paper); display: flex; align-items: center; justify-content: center; text-align: center;
    padding: 14px; font-size: 8px; font-weight: 600; line-height: 10px; color: var(--navy); }

  /* Shared footer */
  .cta { position: absolute; font-family: "Krona One", sans-serif; font-size: 12px; color: var(--paper); letter-spacing: 0.2px; white-space: nowrap; }
  .hotline { position: absolute; display: flex; align-items: center; gap: 7px; font-family: "Krona One", sans-serif; font-size: 18px; color: var(--paper); white-space: nowrap; }
  .hotline svg { width: 26px; height: 20px; }
  .web-lines { position: absolute; font-size: 8.6px; line-height: 12.5px; color: var(--paper); white-space: nowrap; }
  .web-lines__site { font-weight: 700; letter-spacing: 0.4px; }

  /* Back */
  .owner { position: absolute; left: 236px; top: 50px; white-space: nowrap; }
  .owner__name { font-size: 14.5px; color: var(--paper); }
  .owner__role { font-size: 13px; font-weight: 700; color: var(--gold); letter-spacing: 0.5px; margin-top: 5px; }

  .cert-tag { position: absolute; left: 282px; top: 117px; font-family: "Krona One", sans-serif; font-size: 8.5px; color: var(--paper); white-space: nowrap; }

  .pitch { position: absolute; left: 236px; top: 136px; width: 270px; font-size: 10.4px; line-height: 12.8px; color: var(--ink); }
  .pitch span { display: block; white-space: nowrap; }

  .direct-line { position: absolute; left: 240px; top: 230px; display: flex; align-items: center; gap: 5px;
    font-family: "Krona One", sans-serif; font-size: 14px; color: var(--paper); white-space: nowrap; }
  .direct-line svg { width: 18px; height: 14px; }
  .direct-mail { position: absolute; left: 236px; top: 259px; font-size: 10.5px; color: var(--ink); display: flex; align-items: center; gap: 4px; }
  .direct-web { position: absolute; left: 236px; top: 272px; font-size: 11.5px; font-weight: 700; color: var(--ink); letter-spacing: 0.3px; }

  .about-label { position: absolute; left: 39px; top: 318px; font-family: "Krona One", sans-serif; font-size: 22px; color: var(--gold); }
  .about-rule { position: absolute; left: 156px; top: 307px; width: 1px; height: 36px; background: var(--gold); }
  .about-text { position: absolute; left: 165px; top: 311px; width: 335px; font-size: 10px; line-height: 12px; color: var(--ink); }

  .merit { position: absolute; top: 361px; width: 150px; height: 127px; color: var(--paper);
    font-weight: 700; font-style: italic; font-size: 14px; line-height: 17px; text-transform: uppercase; text-align: center; }
  .merit svg { position: absolute; width: 44px; height: 52px; }
  .merit__label { position: absolute; width: 130px; }
  .merit--service { left: 32px; }
  .merit--degree { left: 176px; }
  .merit--clearance { left: 318px; }
</style>
</head>
<body>

<!-- FRONT PAGE -->
<section class="page page--front" aria-label="Flyer front">
  <svg class="page__shapes" viewBox="0 0 508 655" xmlns="http://www.w3.org/2000/svg">
    <polygon points="385,0 508,0 508,371 471,468 210,468" fill="#2a2d4a" role="img" aria-label="Photo of the captain in pirate costume aboard the boat"/>
    <polygon points="0,29 390,29 306,170 0,170" fill="var(--red)"/>
    <polygon points="0,0 440,0 390,29 0,29" fill="var(--paper)"/>

    <polygon points="48,302 68,302 33,376 15,376" fill="var(--red)"/>
    <polygon points="66,302 173,302 126,425 26,425" fill="var(--gold)"/>
    <polygon points="70,305 168,305 123,422 31,422" fill="#5b7d8e" role="img" aria-label="Photo of a student tying a line at the dock"/>
    <polygon points="178,302 280,302 231,425 132,425" fill="var(--gold)"/>
    <polygon points="182,305 275,305 228,422 137,422" fill="#7c8f6a" role="img" aria-label="Photo of a student launching a boat at the ramp"/>
    <polygon points="73,433 173,433 123,557 26,557" fill="var(--gold)"/>
    <polygon points="77,436 168,436 120,554 31,554" fill="#6e7478" role="img" aria-label="Photo of a student working the anchor windlass"/>

    <polygon points="508,386 508,655 56,655 86,571 431,571" fill="var(--charcoal)"/>
    <polygon points="33,655 66,603 82,603 51,655" fill="var(--red)"/>
    <polygon points="63,580 387,580 379,606 54,606" fill="var(--red)"/>

    <circle cx="216" cy="518" r="34" fill="#2b3f7a"/>
    <circle cx="299" cy="518" r="35" fill="var(--navy)"/>
    <circle cx="384" cy="518" r="34" fill="#c7243a"/>
  </svg>

  <div class="brand-seal">Harbor Finch Sailing School &amp; Cruises, LLC</div>

  <h1 class="title display">
    <span class="title__line title__line--lead">Lagoon</span>
    <span class="title__line title__line--mid">Voyage</span>
    <span class="title__line title__line--last">Drawing</span>
  </h1>

  <p class="intro">
    <span>This lagoon voyage is for a boat outing leaving</span>
    <span>from Clearwater going to a barrier island such as</span>
    <span>Anclote or Three Rooker. This package includes</span>
    <span>the boat, a licensed captain and fuel. The</span>
    <span>duration will be approximately four to six hours.</span>
    <span>The winner of the drawing may bring up to a total</span>
    <span>of six passengers. The winner is responsible</span>
    <span>for their own provisions such as ice,</span>
    <span>drinks and food.</span>
  </p>

  <div class="cta" style="left:76px; top:587px;">TO INQUIRE SEND A TEXT TODAY!</div>
  <div class="hotline" style="left:92px; top:617px;">
    <svg viewBox="0 0 28 22"><path d="M2 7 Q14 -1 26 7 L24 10 L19 9 L19 6 Q14 4 9 6 L9 9 L4 10 Z" fill="var(--gold)"/><path d="M7 10 L21 10 L25 21 L3 21 Z" fill="var(--gold)"/><circle cx="14" cy="15" r="3" fill="var(--charcoal)"/></svg>
    <span>(555) 014-2286</span>
  </div>
  <div class="web-lines" style="left:350px; top:617px;">
    <div>✉ hello@harborfinchsail.com</div>
    <div class="web-lines__site">www.harborfinchsail.com</div>
  </div>
</section>

<!-- BACK PAGE -->
<section class="page page--back" aria-label="Flyer back">
  <svg class="page__shapes" viewBox="0 0 510 658" xmlns="http://www.w3.org/2000/svg">
    <polygon points="0,0 289,0 189,286 0,286" fill="var(--navy)" role="img" aria-label="Portrait photo of the owner and captain in a grey polo shirt"/>
    <polygon points="219,41 510,41 510,96 196,96" fill="var(--red)"/>
    <polygon points="273,113 451,113 443,132 266,132" fill="var(--gold)"/>
    <polygon points="233,227 438,227 429,251 224,251" fill="var(--red)"/>

    <polygon points="0,300 510,300 510,658 0,658" fill="var(--mist)" opacity="0.35"/>

    <polygon points="53,361 193,361 148,488 21,488" fill="var(--red)"/>
    <polygon points="206,361 333,361 291,488 162,488" fill="var(--slate)"/>
    <polygon points="346,361 474,361 432,488 303,488" fill="var(--red)"/>

    <circle cx="217" cy="520" r="34" fill="#2b3f7a"/>
    <circle cx="300" cy="520" r="35" fill="var(--navy)"/>
    <circle cx="385" cy="520" r="34" fill="#c7243a"/>

    <polygon points="510,381 510,658 56,658 88,573 433,573" fill="var(--charcoal)"/>
    <polygon points="33,658 66,606 82,606 51,658" fill="var(--red)"/>
    <polygon points="61,583 389,583 382,610 56,610" fill="var(--red)"/>
  </svg>

  <div class="owner">
    <div class="owner__name display">Dalton R. Whitcombe</div>
    <div class="owner__role">OWNER &amp; CAPTAIN</div>
  </div>

  <div class="cert-tag">CERTIFIED INSTRUCTOR</div>

  <p class="pitch">
    <span style="margin-left:27px">Don't overpay elsewhere. All training that is</span>
    <span style="margin-left:21px">conducted by any qualified person or</span>
    <span style="margin-left:15px">company is based off of nationally accredited</span>
    <span style="margin-left:10px">and recognized content and curriculum</span>
    <span style="margin-left:5px">developed by the National Boating Safety Board</span>
    <span>or the United Boating Guilds.</span>
  </p>

  <div class="direct-line">
    <svg viewBox="0 0 28 22"><path d="M2 7 Q14 -1 26 7 L24 10 L19 9 L19 6 Q14 4 9 6 L9 9 L4 10 Z" fill="var(--paper)"/><path d="M7 10 L21 10 L25 21 L3 21 Z" fill="var(--paper)"/><circle cx="14" cy="15" r="3" fill="var(--red)"/></svg>
    <span>(555) 014-2286</span>
  </div>
  <div class="direct-mail"><span style="color:var(--red)">✉</span> hello@harborfinchsail.com</div>
  <div class="direct-web">www.HarborFinchSail.com</div>

  <div class="about-label">ABOUT</div>
  <div class="about-rule"></div>
  <p class="about-text">Federally Licensed Master Captain &amp; National Boating Safety Board Certified Boating Instructor providing hands-on boat training &amp; captaining services with your boat at your location.</p>

  <div class="merit merit--service">
    <svg viewBox="0 0 44 52" style="left:50px; top:10px;">
      <polygon points="22,0 26,9 36,9 28,15 31,25 22,19 13,25 16,15 8,9 18,9" fill="var(--paper)"/>
      <polygon points="6,28 22,36 38,28 38,36 22,44 6,36" fill="var(--paper)"/>
      <polygon points="6,40 22,48 38,40 38,46 22,52 6,46" fill="var(--paper)"/>
    </svg>
    <div class="merit__label" style="left:2px; top:76px;">Retired<br>Military</div>
  </div>

  <div class="merit merit--degree">
    <svg viewBox="0 0 44 52" style="left:50px; top:10px;">
      <polygon points="4,7 22,0 40,7 22,14" fill="var(--paper)"/>
      <rect x="12" y="10" width="20" height="6" fill="var(--paper)"/>
      <rect x="9" y="20" width="26" height="30" fill="none" stroke="var(--paper)" stroke-width="3"/>
      <line x1="14" y1="28" x2="26" y2="28" stroke="var(--paper)" stroke-width="2"/>
      <line x1="14" y1="34" x2="26" y2="34" stroke="var(--paper)" stroke-width="2"/>
      <line x1="14" y1="40" x2="22" y2="40" stroke="var(--paper)" stroke-width="2"/>
      <circle cx="35" cy="38" r="6" fill="var(--paper)"/>
    </svg>
    <div class="merit__label" style="left:0; top:76px;">Graduate<br>Degree</div>
  </div>

  <div class="merit merit--clearance">
    <svg viewBox="0 0 44 52" style="left:60px; top:4px;">
      <path d="M22 0 L42 7 L42 24 Q42 42 22 52 Q2 42 2 24 L2 7 Z" fill="var(--paper)"/>
      <circle cx="22" cy="24" r="10" fill="none" stroke="var(--red)" stroke-width="3"/>
      <polyline points="17,24 21,28 28,20" fill="none" stroke="var(--red)" stroke-width="3"/>
    </svg>
    <div class="merit__label" style="left:6px; top:66px;">Current<br>Security<br>Clearance</div>
  </div>

  <div class="cta" style="left:76px; top:590px;">TO INQUIRE SEND A TEXT TODAY!</div>
  <div class="hotline" style="left:92px; top:620px;">
    <svg viewBox="0 0 28 22"><path d="M2 7 Q14 -1 26 7 L24 10 L19 9 L19 6 Q14 4 9 6 L9 9 L4 10 Z" fill="var(--gold)"/><path d="M7 10 L21 10 L25 21 L3 21 Z" fill="var(--gold)"/><circle cx="14" cy="15" r="3" fill="var(--charcoal)"/></svg>
    <span>(555) 014-2286</span>
  </div>
  <div class="web-lines" style="left:352px; top:620px;">
    <div>✉ hello@harborfinchsail.com</div>
    <div class="web-lines__site">www.harborfinchsail.com</div>
  </div>
</section>

</body>
</html>
```